Business Card Design

We like to use greens as you will see in our logo (but not TOO much green). We are a Dental Clinic in a somewhat eccentric community. We do not like the dated sharp designs which we see many dentists use. We're looking for something bright and fresh while still maintaining the integrity of the profession. Elegance is not necessarily what we are going for... we need for the design to be "mature" but also up-lifting.

See our logo.
Updates

Project Deadline Extended
Reason: We have 5 designs which we like. But we'd like to see a few more before committing to a design.

Project Deadline Extended
Reason: We are awaiting revisions to this project. We are still welcoming designs while we wait to see if designers are able to provide to us the revisions we require in order to proceed with a selection.

Target Market(s)

Younger families - ages late 20's to early 40's

Industry/Entity Type

Business

Contact Information for Business Card

Marlow T. Benning DDS 2740 W. Hollister Rd. Ste. 7 Royal Oak, MI 48133 (248)555-0193 FX (248)555-0147 info@BrightwellDentalCareMi.example BrigthwellDentalCareMi.example on the back of the card we need an appointment reminder (For____ Date___ Time____) with "If you are unable to keep your appointment, kindly give 48 hours notice" at the bottom. No use of teeth in the design. DOUBLE SIDED DESIGN

Requirements
Should not have
• The use of pictures of teeth

```html
<!DOCTYPE html>
<html lang="en">
<head>
<meta charset="utf-8">
<title>Brightwell Dental Care – Business Card</title>
<link rel="stylesheet" href="https://fonts.googleapis.com/css2?family=Open+Sans:wght@400;600&family=Tinos:ital,wght@0,700;1,400&display=swap">
<style>
  :root {
    --stage: #e9e7e3;
    --card: #ffffff;
    --lime: #7ed321;
    --lime-bright: #8ee02a;
    --forest: #2f7a12;
    --ink: #3a3a3a;
    --muted: #6a6a6a;
    --rule: #8a8a8a;
  }
  * { box-sizing: border-box; margin: 0; padding: 0; }
  html, body { width: 1200px; height: 492px; overflow: hidden; }
  body {
    background: var(--stage);
    font-family: "Open Sans", Arial, sans-serif;
    position: relative;
  }
  .card {
    position: absolute;
    top: 96px;
    width: 520px;
    height: 300px;
    background: var(--card);
    box-shadow: 0 6px 18px rgba(0,0,0,.18);
    overflow: hidden;
  }
  .card--front { left: 50px; }
  .card--back { left: 630px; }

  .front-band { position: absolute; inset: 0; }

  .brand {
    position: absolute;
    display: flex;
    align-items: center;
    gap: 10px;
    color: var(--forest);
    font-weight: 600;
    line-height: 1.05;
  }
  .brand__dot {
    width: 16px; height: 16px; border-radius: 50%;
    background: var(--lime);
    flex: none;
  }
  .card--front .brand { left: 30px; top: 120px; font-size: 25px; }
  .card--back .brand { left: 36px; top: 52px; font-size: 25px; }

  .contact {
    position: absolute;
    right: 20px;
    top: 26px;
    text-align: right;
    color: #fff;
  }
  .contact__name { font-size: 19px; margin-bottom: 22px; }
  .contact__name small { font-size: 13px; }
  .contact__address { font-size: 12.5px; line-height: 1.4; margin-bottom: 26px; }
  .contact__line {
    font-size: 11.5px;
    line-height: 1.8;
    display: flex;
    justify-content: flex-end;
    align-items: center;
    gap: 5px;
    white-space: nowrap;
  }
  .contact__line svg { width: 11px; height: 11px; fill: #fff; flex: none; }

  .appointment {
    position: absolute;
    left: 36px;
    top: 168px;
    right: 30px;
    color: var(--ink);
  }
  .appointment__title {
    font-family: "Tinos", "Times New Roman", serif;
    font-weight: 700;
    font-size: 15px;
    color: var(--forest);
    letter-spacing: .3px;
    margin-bottom: 18px;
  }
  .appointment__row {
    display: flex;
    align-items: flex-end;
    font-size: 13px;
    margin-bottom: 14px;
    white-space: nowrap;
  }
  .field-line {
    display: inline-block;
    border-bottom: 1px solid var(--rule);
    height: 12px;
    margin: 0 6px 2px;
  }
  .field-line--dotted { border-bottom-style: dotted; }
  .appointment__note {
    font-family: "Tinos", "Times New Roman", serif;
    font-style: italic;
    font-size: 13.5px;
    color: var(--muted);
    margin-top: 10px;
  }
</style>
</head>
<body>

<section class="card card--front" aria-label="Business card front">
  <svg class="front-band" viewBox="0 0 520 300" width="520" height="300" aria-hidden="true">
    <path d="M212,0 C254,100 258,200 236,300 L520,300 L520,0 Z" fill="var(--lime-bright)"/>
    <path d="M196,0 C238,100 242,200 220,300" fill="none" stroke="var(--forest)" stroke-width="5"/>
  </svg>

  <div class="brand">
    <span class="brand__dot"></span>
    <span>Brightwell<br>Dental Care</span>
  </div>

  <div class="contact">
    <p class="contact__name">Marlow T. Benning <small>DDS</small></p>
    <p class="contact__address">2740 W. Hollister Rd. Ste. 7<br>Royal Oak, MI 48133</p>
    <p class="contact__line">
      <svg viewBox="0 0 24 24"><path d="M6.6 10.8a15 15 0 0 0 6.6 6.6l2.2-2.2c.3-.3.7-.4 1-.2 1.1.4 2.3.6 3.6.6.6 0 1 .4 1 1V20c0 .6-.4 1-1 1A17 17 0 0 1 3 4c0-.6.4-1 1-1h3.5c.6 0 1 .4 1 1 0 1.3.2 2.5.6 3.6.1.3 0 .7-.2 1z"/></svg>
      (248)555-0193
    </p>
    <p class="contact__line">
      <svg viewBox="0 0 24 24"><path d="M6 2h12v6H6zM4 9h16a2 2 0 0 1 2 2v6h-4v5H6v-5H2v-6a2 2 0 0 1 2-2zm4 8v3h8v-3z"/></svg>
      (248)555-0147
    </p>
    <p class="contact__line">
      <svg viewBox="0 0 24 24"><path d="M2 5h20v14H2zm2 2v.5l8 5 8-5V7zm0 2.8V17h16V9.8l-8 5z"/></svg>
      info@BrightwellDentalCareMi.example
    </p>
    <p class="contact__line">
      <svg viewBox="0 0 24 24"><path d="M12 2a10 10 0 1 0 0 20 10 10 0 0 0 0-20zm-1 2.1V8H7.3A8 8 0 0 1 11 4.1zm2 0A8 8 0 0 1 16.7 8H13zM4.3 10H11v4H4.3a8 8 0 0 1 0-4zM13 10h6.7a8 8 0 0 1 0 4H13zm-5.7 6H11v3.9A8 8 0 0 1 7.3 16zM13 16h3.7a8 8 0 0 1-3.7 3.9z"/></svg>
      www.BrigthwellDentalCareMi.example
    </p>
  </div>
</section>

<section class="card card--back" aria-label="Business card back, appointment reminder">
  <div class="brand">
    <span class="brand__dot"></span>
    <span>Brightwell<br>Dental Care</span>
  </div>

  <div class="appointment">
    <h2 class="appointment__title">YOUR APPOINTMENT</h2>
    <p class="appointment__row">Name :<span class="field-line field-line--dotted" style="width:260px"></span></p>
    <p class="appointment__row">Date :<span class="field-line" style="width:90px"></span>&nbsp;&nbsp;&nbsp;Time :<span class="field-line" style="width:85px"></span>am / pm</p>
    <p class="appointment__note">If you are unable to keep your appointment, kindly give 48 hours notice</p>
  </div>
</section>

</body>
</html>
```